'Ormel Property Development' Business Card

Business Card Features:

High Quality (potentially textured) thick card - preference is white textured card

Logo (supplied)

We plan to use the vertical logo as the main logo. But i am happy for people to use either if they find it works better for the design of the card.

The building icon and also the insert to the 'E' is in a metallic finish, i think this should be finished in a metallic embossed or raised style.
Updates

Please note i have attached both a horizontal and Vertical Logo for your reference. We plan to use the vertical logo as the main logo. But i am happy for people to use either if they find it works better for the design of the card.

Please note i am considering having the cards made on stainless steel. This introduces the option of having cut outs in the card and etching or printing for the design. If you have a good concept for this please submit.

http://www.tinquarry.example/black-metal-cards# this is a site that makes the metal cards to offer some direction . . . . Please note i am basic the selection o the best design, if that means normal print cards on paper then this is what i will choose. But there are some great options with the metal. Thanks.

Industry/Entity Type

Building

Requirements
Must have
• Helvetica font to details side of card - logo as supplied to opposite side.

Card Details:

Darrow Pketts
Managing Director

+61 487 263 518
+61 3 6172 4809

PO Box 73
Bentleigh, VIC 3024

darrow@ormel.example

www.ormel.example

```html
<!DOCTYPE html>
<html lang="en">
<head>
<meta charset="utf-8">
<title>Ormel Property Development – Business Card</title>
<link href="https://fonts.googleapis.com/css2?family=Arimo:wght@400;700&display=swap" rel="stylesheet">
<style>
  :root {
    --page-bg: #ffffff;
    --steel-dark: #7f7f9e;
    --steel-mid: #a9b7c9;
    --steel-light: #e9f1f5;
    --steel-cool: #bcd0de;
    --etch: #ffffff;
    --etch-shadow: rgba(40, 45, 70, 0.55);
    --note-ink: #111111;
  }
  * { box-sizing: border-box; margin: 0; padding: 0; }
  html, body {
    width: 1200px;
    height: 1000px;
    overflow: hidden;
    background: var(--page-bg);
    font-family: "Arimo", Helvetica, Arial, sans-serif;
  }
  .canvas {
    position: relative;
    width: 1200px;
    height: 1000px;
  }
  .card {
    position: absolute;
    left: 130px;
    top: 150px;
    width: 940px;
    height: 598px;
    border-radius: 46px;
    overflow: hidden;
    background: linear-gradient(90deg,
      var(--steel-dark) 0%,
      var(--steel-mid) 18%,
      var(--steel-cool) 34%,
      var(--steel-light) 52%,
      var(--steel-cool) 66%,
      var(--steel-light) 82%,
      var(--steel-mid) 100%);
    box-shadow: 0 2px 6px rgba(0,0,0,0.15);
  }
  .brand {
    position: absolute;
    left: 0;
    right: 0;
    top: 200px;
    text-align: center;
    color: var(--etch);
  }
  .brand-mark {
    display: block;
    width: 26px;
    height: 26px;
    margin: 0 auto 14px;
    background: var(--etch);
  }
  .brand-name {
    display: block;
    font-weight: 700;
    font-size: 78px;
    letter-spacing: 4px;
    line-height: 1;
  }
  .brand-tagline {
    display: block;
    margin-top: 8px;
    font-weight: 700;
    font-size: 20px;
    letter-spacing: 1px;
  }
  .divider {
    position: absolute;
    left: 28px;
    right: 28px;
    top: 372px;
    height: 4px;
    background: var(--etch);
    border-radius: 2px;
  }
  .details {
    position: absolute;
    left: 0;
    right: 0;
    top: 398px;
    color: var(--etch);
    text-align: center;
    font-weight: 700;
    text-shadow: 1px 1px 2px var(--etch-shadow);
  }
  .person-name { font-size: 27px; line-height: 1.1; }
  .person-role { font-size: 14px; margin-top: 2px; }
  .contact-list {
    margin-top: 36px;
    font-size: 21px;
    line-height: 29px;
  }
  .contact-row {
    display: flex;
    justify-content: center;
    gap: 60px;
  }
  .contact-row span { min-width: 0; }
  .note {
    position: absolute;
    left: 0;
    right: 0;
    top: 790px;
    text-align: center;
    font-weight: 700;
    font-size: 22px;
    color: var(--note-ink);
  }
</style>
</head>
<body>
<main class="canvas">
  <section class="card" aria-label="Stainless steel business card">
    <div class="brand">
      <span class="brand-mark" aria-hidden="true"></span>
      <span class="brand-name">ORMEL</span>
      <span class="brand-tagline">Property Development</span>
    </div>
    <div class="divider" aria-hidden="true"></div>
    <div class="details">
      <p class="person-name">Darrow Pketts</p>
      <p class="person-role">Managing Director</p>
      <div class="contact-list">
        <p class="contact-row"><span>ADDRESS: PO BOX 73 Bentleigh, VIC 3024</span></p>
        <p class="contact-row"><span>TEL: 0487263518</span><span>MOB: 1800 642 917</span></p>
        <p class="contact-row"><span>EMAIL: darrow@ormel.example</span><span>WEBSITE: www.ormel.example</span></p>
      </div>
    </div>
  </section>
  <p class="note">Note: Only the logo and the straight in he business cut will be cut off.</p>
</main>
</body>
</html>
```